Brindle Lawyers Banner

I would like to have a graphic design created for a company banner. The company is Brindle Lawyers and the website is https://brindlelawyers.example.au/ We would like a professional banner we are able to put up at events to advertise the company.
The banner size is 800mm wide by 2000mm high so please keep the design inside these constraints.

```html
<!DOCTYPE html>
<html lang="en">
<head>
<meta charset="utf-8">
<title>Brindle Lawyers – Event Banner</title>
<link rel="stylesheet" href="https://fonts.googleapis.com/css2?family=Montserrat:wght@400;500;600;700;800&family=Oswald:wght@700&display=swap">
<style>
  :root{
    --ink:#2b2d31;
    --brand-blue:#27a2d7;
    --brand-yellow:#f6b71b;
    --sage:#a1c4bd;
    --paper:#ffffff;
    --card:#f0f1f2;
    --backdrop:#e4e5e6;
    --photo-top:#eef3f6;
    --photo-bottom:#6d7f8c;
  }
  *{margin:0;padding:0;box-sizing:border-box}
  html,body{width:1200px;height:1055px;overflow:hidden;background:var(--backdrop)}
  .banner{position:absolute;left:408px;top:48px;width:384px;height:960px;box-shadow:0 10px 28px rgba(0,0,0,.18)}
  .banner svg{display:block}
  .fill-paper{fill:var(--paper)}
  .fill-ink{fill:var(--ink)}
  .fill-blue{fill:var(--brand-blue)}
  .fill-yellow{fill:var(--brand-yellow)}
  .fill-card{fill:var(--card)}
  .wordmark{font-family:'Montserrat',sans-serif;font-weight:400;fill:var(--ink)}
  .headline{font-family:'Montserrat',sans-serif}
  .headline-lead{font-weight:800;fill:var(--sage);font-size:46px}
  .headline-body{font-weight:500;fill:var(--paper);font-size:21px}
  .headline-blue{font-weight:800;fill:var(--brand-blue);font-size:27px}
  .headline-yellow{font-weight:800;fill:var(--brand-yellow);font-size:31px}
  .help-title{font-family:'Oswald',sans-serif;font-weight:700;font-size:25px;fill:var(--ink)}
  .card-label{font-family:'Montserrat',sans-serif;font-weight:600;font-size:11.5px;fill:var(--ink)}
  .phone{font-family:'Montserrat',sans-serif;font-weight:800;font-size:36px;fill:var(--paper)}
  .web{font-family:'Montserrat',sans-serif;font-weight:500;font-size:22px;fill:var(--paper)}
  .icon-ring{fill:var(--ink);stroke:var(--brand-blue);stroke-width:2}
  .icon-line{fill:none;stroke:var(--brand-yellow);stroke-width:1.6;stroke-linecap:round;stroke-linejoin:round}
</style>
</head>
<body>
<div class="banner">
<svg width="384" height="960" viewBox="0 0 384 960" xmlns="http://www.w3.org/2000/svg">
  <defs>
    <linearGradient id="photoTone" x1="0" y1="0" x2="0" y2="1">
      <stop offset="0" stop-color="var(--photo-top)"/>
      <stop offset="1" stop-color="var(--photo-bottom)"/>
    </linearGradient>
  </defs>

  <rect class="fill-paper" width="384" height="960"/>

  <!-- team photo area -->
  <g role="img" aria-label="Photo of a group of business people shaking hands in a bright office">
    <rect x="0" y="150" width="384" height="220" fill="url(#photoTone)"/>
  </g>

  <!-- wordmark -->
  <text class="wordmark" x="328" y="110" font-size="54" text-anchor="end">BRINDLE</text>
  <text class="wordmark" x="328" y="138" font-size="18" letter-spacing="4" text-anchor="end">LAWYERS</text>

  <!-- dark band -->
  <polygon class="fill-ink" points="0,275 384,362 384,515 0,605"/>

  <!-- headline -->
  <g class="headline">
    <text class="headline-lead" x="112" y="398">Leading</text>
    <text class="headline-body" x="113" y="422">commercial</text>
    <text x="112" y="454"><tspan class="headline-blue">Law Firm</tspan><tspan class="headline-body" dx="8">located</tspan></text>
    <text class="headline-body" x="113" y="481">in Logan City,</text>
    <text class="headline-yellow" x="112" y="512">Queensland.</text>
  </g>

  <!-- help ribbon -->
  <polygon class="fill-yellow" points="50,553 347,553 335,596 37,596"/>
  <text class="help-title" x="192" y="586" text-anchor="middle" transform="skewX(-8) translate(82,0)">HOW CAN WE HELP YOU?</text>

  <!-- service cards -->
  <g class="services">
    <rect class="fill-card" x="44" y="646" width="133" height="62"/>
    <rect class="fill-card" x="193" y="646" width="137" height="62"/>
    <rect class="fill-card" x="44" y="748" width="133" height="62"/>
    <rect class="fill-card" x="193" y="748" width="137" height="62"/>

    <circle class="icon-ring" cx="111" cy="635" r="25"/>
    <g class="icon-line">
      <rect x="103" y="622" width="16" height="22"/>
      <path d="M107,628 H116 M107,633 H116 M107,638 H113"/>
    </g>
    <circle class="icon-ring" cx="262" cy="635" r="25"/>
    <g class="icon-line">
      <path d="M251,635 L262,625 L273,635 V645 H251 Z"/>
      <rect x="258" y="637" width="8" height="8"/>
    </g>
    <circle class="icon-ring" cx="111" cy="741" r="25"/>
    <g class="icon-line">
      <circle cx="111" cy="734" r="4"/>
      <path d="M103,748 Q111,738 119,748"/>
      <path d="M98,738 V750 L106,756 M124,738 V750 L116,756"/>
    </g>
    <circle class="icon-ring" cx="262" cy="741" r="25"/>
    <g class="icon-line">
      <rect x="252" y="730" width="14" height="10" rx="2"/>
      <rect x="260" y="735" width="14" height="10" rx="2"/>
      <path d="M252,754 H274"/>
    </g>

    <text class="card-label" x="111" y="682" text-anchor="middle">Private Clients and</text>
    <text class="card-label" x="111" y="696" text-anchor="middle">Family Businesses</text>
    <text class="card-label" x="262" y="683" text-anchor="middle">Startups and</text>
    <text class="card-label" x="262" y="697" text-anchor="middle">New Businesses</text>
    <text class="card-label" x="111" y="784" text-anchor="middle">Established</text>
    <text class="card-label" x="111" y="798" text-anchor="middle">Organisations</text>
    <text class="card-label" x="262" y="785" text-anchor="middle">Professional</text>
    <text class="card-label" x="262" y="799" text-anchor="middle">Advisors</text>
  </g>

  <!-- contact -->
  <polygon class="fill-blue" points="0,888 384,800 384,960 0,960"/>
  <polygon class="fill-yellow" points="50,826 347,826 335,869 37,869"/>
  <text class="phone" x="192" y="861" text-anchor="middle">07 5550 1824</text>
  <text class="web" x="192" y="900" text-anchor="middle">brindlelawyers.example.au</text>
</svg>
</div>
</body>
</html>
```